Consumer Finance flyer

This flyer is being developed to help our outside sales people.

Please develop a master template flyer with key bullet points similar to uploaded file.

The main graphic will be replaced as we build out a flyer for each market segment. Example: Healthcare, Dental, Remodeling etc.
so we will keep the bullet point but replace the graphic for each custom vertical industry.

Need flyer to have an editable section at the bottom so the sales person can add their name and phone number and print the flyer.

please incorporate the FundLeafOne logo attached. So it will be branded fundleafone.

Industry/Entity Type

Dental

```html
<!DOCTYPE html>
<html lang="en">
<head>
<meta charset="utf-8">
<title>FundLeafOne – A New Financing Focus</title>
<link rel="stylesheet" href="https://fonts.googleapis.com/css2?family=Dosis:wght@600;700&family=Crimson+Text:wght@400&family=Alegreya+Sans:wght@400&display=swap">
<style>
  :root {
    --page: #ffffff;
    --sky: #7ccbec;
    --sky-deep: #4fa9cf;
    --gold: #f5b70c;
    --white: #ffffff;
    --panel-blue: #69abcb;
    --ink: #1d1d1d;
    --bullet-ink: #8a5a1c;
    --office-light: #dfe6ea;
    --office-dark: #8e9aa2;
    --pig-pink: #f2a3a3;
    --pig-blue: #9fb9d3;
  }
  * { margin: 0; padding: 0; box-sizing: border-box; }
  html, body { width: 857px; height: 1200px; overflow: hidden; background: var(--page); }
  .flyer { position: relative; width: 857px; height: 1200px; background: var(--page); }

  .hero-banner {
    position: absolute; left: 18px; top: 18px; width: 815px; height: 214px;
    background: linear-gradient(160deg, #9ad8f1 0%, var(--sky) 45%, var(--sky-deep) 100%);
  }
  .headline { position: absolute; font-family: "Dosis", sans-serif; font-weight: 700; text-transform: uppercase; line-height: 1; }
  .headline-a { left: 60px; top: 30px; font-size: 74px; color: var(--white); letter-spacing: 2px; }
  .headline-financing { left: 208px; top: 84px; font-size: 96px; color: var(--gold); letter-spacing: 3px; }
  .headline-focus { left: 562px; top: 144px; font-size: 82px; color: var(--white); letter-spacing: 3px; }

  .feature-photo {
    position: absolute; left: 18px; top: 250px; width: 469px; height: 312px;
    background: linear-gradient(135deg, var(--office-light) 0%, #c4ced4 55%, var(--office-dark) 100%);
  }
  .intro-panel {
    position: absolute; left: 18px; top: 574px; width: 469px; height: 392px;
    background: var(--panel-blue); padding: 18px 18px 0 18px;
    font-family: "Crimson Text", serif; font-size: 19.5px; line-height: 27px; color: var(--ink);
  }
  .intro-copy { text-align: justify; margin-bottom: 27px; }
  .services { list-style: none; }
  .piggy-photo {
    position: absolute; left: 18px; top: 985px; width: 469px; height: 148px;
    background: linear-gradient(90deg, var(--pig-pink) 0%, #f6c1c1 40%, var(--pig-blue) 60%, var(--pig-pink) 100%);
  }

  .benefits-panel {
    position: absolute; left: 503px; top: 248px; width: 330px; height: 882px;
    background: var(--gold);
  }
  .benefits {
    list-style: none; position: absolute; left: 18px; top: 22px;
    font-family: "Crimson Text", serif; font-size: 17px; letter-spacing: 0.6px;
    color: var(--bullet-ink); line-height: 43px; white-space: nowrap;
  }
  .brand {
    position: absolute; left: 18px; top: 676px; display: flex; align-items: center; gap: 8px;
    font-family: "Alegreya Sans", sans-serif; font-size: 33px; letter-spacing: 2px; color: var(--ink);
  }
  .brand-dot { width: 14px; height: 14px; border-radius: 50%; background: var(--ink); }
  .rep-contact {
    position: absolute; left: 24px; top: 744px;
    font-family: "Alegreya Sans", sans-serif; font-size: 33px; line-height: 39px; color: var(--ink);
  }
</style>
</head>
<body>
<main class="flyer">
  <div class="hero-banner" role="img" aria-label="Fanned stack of dollar bills tinted sky blue"></div>
  <h1>
    <span class="headline headline-a">A New</span>
    <span class="headline headline-financing">Financing</span>
    <span class="headline headline-focus">Focus</span>
  </h1>

  <div class="feature-photo" role="img" aria-label="Industry photo: two business professionals in a bright open-plan office"></div>

  <section class="intro-panel">
    <p class="intro-copy">Multiple lenders will process your clients with only ONE credit application. We will contact your clients for security and to help expedite the lending process for optimum performance and satisfaction. Co-borrowers are welcome to help income profile of your clients. This can overcomereservations.</p>
    <ul class="services">
      <li>We provide:</li>
      <li>Custom application website</li>
      <li>Online payment calculators.</li>
      <li>Back office status access.</li>
      <li>Live assistance.</li>
      <li>*multiple programs available*</li>
    </ul>
  </section>

  <div class="piggy-photo" role="img" aria-label="Row of pink and blue piggy banks"></div>

  <aside class="benefits-panel">
    <ul class="benefits">
      <li>SEVERAL INTEREST FREE PLANS</li>
      <li>0% FOR 6 TO 18 MONTHS</li>
      <li>REVOLVING LINES OF CREDIT</li>
      <li>TERM LOANS FROM 2 TO 20YRS</li>
      <li>NATIONAL LENDERS COMPETE</li>
      <li>EASY SINGLE PAGE APP</li>
      <li>LENIENT REQUIREMENTS</li>
      <li>NO DEFAULT INTEREST RATES</li>
      <li>NO PREPAYMENT PENALTIES</li>
      <li>MAY REQUEST OVERNIGHT</li>
      <li>RATES FROM 6.95%*</li>
      <li>&nbsp;LUS NO CREDIT APP OPTION</li>
      <li>&nbsp;APPROVALS IN MINUTES</li>
      <li>MAY COMBINE OFFERS</li>
      <li>CREDIT APPROVALS 24 TO 48 HRS</li>
    </ul>
    <div class="brand"><span>FUNDLEAFONE</span><span class="brand-dot"></span></div>
    <address class="rep-contact" contenteditable="true" style="font-style:normal">
      866-555-0142<br>
      Dana Wells<br>
      dana@fundleafone.net
    </address>
  </aside>
</main>
</body>
</html>
```